"A Touch RMB" Business Card/Logo Design

I'm looking for a very creative look for my new business called "A Touch RMB" on a business card design. Don't be distracted by my "business card details" below....if you have other ideas on how you see "A Touch RMB" go for it. If probably should somehow give a look that I paint furniture....maybe a paint drip or something simple or you can get more creative....sky's the limit and I really need your creative eye on how to per tray that "A Touch RMB" means taking something old and turning into new again with some paint.

Industry/Entity Type

Business

Contact Information for Business Card

I refurbish and up-cycle furniture that needs "a little TLC'....thus, my business name was born called "A Touch RMB" (Those are my initials). I mainly paint old furniture of all styles and bring them back to life. I sometimes recreate furniture as well....I will make benches from old headboards of all sizes, etc. I'd love to see design that incorporate the crafty/creative side of me. If that means incorporating a paint brush, tools, paint cans, or furniture such as dressers, old vintage furniture, spindles, etc, etc. I don't know if something creative could be done with my initials (RMB). I really have a creative block of ideas and need your help bringing my "A Touch RMB" business to life.

P.S. Below is just one picture that I thought was neat and creative as they used a paintbrush but used spindles for the bristles and put their logo in the middle. Just an idea I thought was very unique and creative.

I'm very excited to see your design. Thank you for taking the time to create my logo/business card for me.

Carla

Requirements
Must have
• Please include this information on the card:
• My Name: Carla Brennick
• Address: 14706 318th Ln SE, Fox Hollow, MN 55418
• E-Mail: atouchrmb@mailcove.net
• FB: http:/www.friendpage.net/atouchrmb
• Cell: 763-419-7082

```html
<!DOCTYPE html>
<html lang="en">
<head>
<meta charset="utf-8">
<title>A Touch RMB – Business Card</title>
<link rel="stylesheet" href="https://fonts.googleapis.com/css2?family=Open+Sans:wght@400;600;700&display=swap">
<style>
  :root {
    --backdrop: #d8d2c8;
    --card: #0b0b0b;
    --card-sheen: #1c1c1c;
    --accent-red: #e8434f;
    --accent-teal: #8fc6c6;
    --ink-light: #f2f2f2;
    --ink-soft: #cfcfcf;
  }
  * { box-sizing: border-box; margin: 0; padding: 0; }
  html, body {
    width: 1200px;
    height: 1022px;
    overflow: hidden;
    background: var(--backdrop);
    font-family: "Open Sans", Arial, sans-serif;
  }
  .business-card {
    position: absolute;
    left: 150px;
    top: 254px;
    width: 900px;
    height: 514px;
    border-radius: 26px;
    background: linear-gradient(135deg, var(--card-sheen) 0%, var(--card) 55%);
    box-shadow: 0 18px 40px rgba(0,0,0,0.35);
    color: var(--ink-light);
  }
  .brand-mark {
    position: absolute;
    left: 70px;
    top: 300px;
    display: flex;
    align-items: center;
    gap: 16px;
  }
  .brand-dot {
    width: 30px;
    height: 30px;
    border-radius: 50%;
    background: var(--accent-teal);
  }
  .brand-name {
    font-size: 40px;
    font-weight: 600;
    color: var(--accent-red);
    letter-spacing: 0.5px;
  }
  .contact-block {
    position: absolute;
    left: 470px;
    top: 70px;
  }
  .person-name {
    font-size: 36px;
    font-weight: 700;
    color: var(--accent-red);
    line-height: 1.1;
  }
  .person-role {
    font-size: 21px;
    color: var(--ink-light);
    margin-top: 4px;
  }
  .address {
    margin-top: 44px;
    font-size: 21px;
    line-height: 1.4;
    color: var(--ink-light);
  }
  .contact-list {
    list-style: none;
    margin-top: 44px;
    font-size: 20px;
    line-height: 1.55;
    color: var(--ink-light);
  }
  .contact-list li {
    display: flex;
    align-items: center;
    gap: 12px;
  }
  .contact-icon {
    width: 18px;
    height: 18px;
    flex: none;
  }
</style>
</head>
<body>
  <section class="business-card">
    <div class="brand-mark">
      <span class="brand-dot"></span>
      <span class="brand-name">A Touch RMB</span>
    </div>

    <div class="contact-block">
      <h1 class="person-name">Carla Brennick</h1>
      <p class="person-role">Owner</p>

      <p class="address">14706 318th Ln SE<br>Fox Hollow, MN 55418</p>

      <ul class="contact-list">
        <li>
          <svg class="contact-icon" viewBox="0 0 18 18" aria-hidden="true">
            <rect x="4" y="1" width="10" height="16" rx="2" fill="none" stroke="var(--accent-teal)" stroke-width="2"/>
            <circle cx="9" cy="14" r="1.2" fill="var(--accent-teal)"/>
          </svg>
          <span>763-419-7082</span>
        </li>
        <li>
          <svg class="contact-icon" viewBox="0 0 18 18" aria-hidden="true">
            <rect x="1" y="3" width="16" height="12" rx="1.5" fill="none" stroke="var(--accent-teal)" stroke-width="2"/>
            <path d="M2 4 L9 10 L16 4" fill="none" stroke="var(--accent-teal)" stroke-width="2"/>
          </svg>
          <span>atouchrmb@mailcove.net</span>
        </li>
        <li>
          <svg class="contact-icon" viewBox="0 0 18 18" aria-hidden="true">
            <rect x="3" y="3" width="12" height="12" rx="2" fill="var(--accent-teal)"/>
          </svg>
          <span>www.friendpage.net/atouchrmb</span>
        </li>
      </ul>
    </div>
  </section>
</body>
</html>
```